Lakemond Drywork Business Card Design

Professional and clean design. The design colors should flow with the logo. Two-sided card with the website on the back which is:

www.LakemondDrywork.example.

"Specializing in Water Damage Restoration"

On the front I need the name, email, phone, and logo.

Name: Darnell Quimby
Email: Darnell@LakemondDrywork.example
Phone: 555-018-2364 for now

I only have the Preview and Thumbnail right now but should have the source files uploaded within a day or two.

Target Market(s)

Flood victims, home owners with water damage from busted pipes etc...

Industry/Entity Type

Business

Contact Information for Business Card

Name: Darnell Quimby

Font styles to use
Serif
Sans Serif

Requirements
Must have
• Business Card Details Info

```html
<!DOCTYPE html>
<html lang="en">
<head>
<meta charset="utf-8">
<title>Lakemond Drywork – Business Card</title>
<link rel="stylesheet" href="https://fonts.googleapis.com/css2?family=EB+Garamond:wght@400;600&display=swap">
<style>
  :root {
    --stage: #e9e7e3;
    --card-dark: #1f2022;
    --card-grey: #2b2c2e;
    --brand-blue: #3ba9d6;
    --mark-blue: #2f5f78;
    --text-light: #f2f2f2;
    --text-soft: #d6d6d6;
  }
  * { margin: 0; padding: 0; box-sizing: border-box; }
  html, body { width: 1200px; height: 1023px; overflow: hidden; }
  body {
    background: var(--stage);
    font-family: "EB Garamond", Georgia, serif;
    display: flex;
    flex-direction: column;
    align-items: center;
    justify-content: center;
    gap: 56px;
  }
  .card {
    width: 735px;
    height: 420px;
    border-radius: 6px;
    position: relative;
    overflow: hidden;
    box-shadow: 0 10px 28px rgba(0,0,0,.22);
  }
  .card--brand { background: var(--card-dark); }
  .card--contact { background: var(--card-grey); }

  .brand-mark {
    position: absolute;
    left: 40px;
    top: 170px;
    width: 210px;
    height: 210px;
    border-radius: 50%;
    background: var(--mark-blue);
    opacity: .85;
  }
  .brand-copy {
    position: absolute;
    right: 44px;
    top: 96px;
    width: 410px;
    text-align: right;
    white-space: nowrap;
  }
  .brand-name {
    color: var(--brand-blue);
    font-size: 31px;
    font-weight: 400;
    letter-spacing: 2px;
    text-transform: uppercase;
    line-height: 1.1;
  }
  .brand-rule {
    display: block;
    margin: 10px 0 0 auto;
    width: 240px;
    height: 1px;
    background: var(--brand-blue);
  }
  .brand-tagline {
    color: var(--text-light);
    font-size: 21px;
    margin-top: 14px;
  }
  .brand-web {
    color: var(--text-light);
    font-size: 19px;
    font-weight: 600;
    margin-top: 8px;
  }

  .contact-list {
    position: absolute;
    left: 70px;
    top: 50%;
    transform: translateY(-50%);
    list-style: none;
    color: var(--text-soft);
    font-size: 20px;
    line-height: 1.75;
  }
  .contact-name {
    color: var(--brand-blue);
    font-size: 28px;
    letter-spacing: 1px;
    margin-bottom: 10px;
  }
</style>
</head>
<body>
  <section class="card card--brand">
    <div class="brand-mark"></div>
    <div class="brand-copy">
      <h1 class="brand-name">Lakemond Drywork</h1>
      <span class="brand-rule"></span>
      <p class="brand-tagline">Specializing in Water Damage Restoration</p>
      <p class="brand-web">www.LakemondDrywork.example</p>
    </div>
  </section>

  <section class="card card--contact">
    <ul class="contact-list">
      <li class="contact-name">Darnell Quimby</li>
      <li>555-018-2364</li>
      <li>Darnell@LakemondDrywork.example</li>
      <li>chirp.example/LakemondDrywork</li>
      <li>friendpage.example/LakemondDrywork</li>
    </ul>
  </section>
</body>
</html>
```